Kovaridex Website

we need a web site similar to Zumwarp.com or Ostrix9 com or brackfield.com - Although our budget is small we would like to look like them. we are in the same industry
Reason: Can you do an exact copy of Zumwarp.com if so how long ? What do you require? What is the next step?Please let me know you can also email me at tolvaburn@pexmail.com for faster answers.
Thank you
Target Market(s)
small and medium size business
Requirements
Must have
- product portfolio - just like Zumwarp.com
Nice to have
- ecomerce and mobile app

```html
<!DOCTYPE html>
<html lang="en">
<head>
<meta charset="utf-8">
<title>Kovaridex</title>
<link href="https://fonts.googleapis.com/css2?family=Roboto:wght@300;400;500&display=swap" rel="stylesheet">
<style>
:root{
  --green:#80bd01;
  --green-dark:#6fa800;
  --green-text:#6aa700;
  --ink:#333;
  --muted:#555;
  --panel:#e9e9e9;
  --page:#f2f2f2;
  --footer:#3a3a3a;
  --footer-box:#474747;
  --white:#fff;
}
*{box-sizing:border-box;margin:0;padding:0}
html,body{width:866px;height:1200px;overflow:hidden}
body{position:relative;font-family:"Roboto",Arial,sans-serif;color:var(--ink);
  background-color:var(--page);
  background-image:linear-gradient(#e8e8e8 1px,transparent 1px),linear-gradient(90deg,#e8e8e8 1px,transparent 1px);
  background-size:12px 12px}
.abs{position:absolute}
.topbar{left:0;top:0;width:866px;height:18px;background:var(--green-dark)}
.account{left:186px;top:4px;font-size:7px;color:var(--white)}
.account u{margin-left:2px}
.search{left:581px;top:3px;width:100px;height:12px;background:var(--white);font-size:6.5px;color:var(--green-text);padding:2px 6px}
.search svg{position:absolute;right:3px;top:1px}
.header{left:0;top:18px;width:866px;height:53px;background:var(--green)}
.logo{left:186px;top:32px;font-size:20px;font-weight:300;color:var(--white);letter-spacing:-.5px}
.logo-dot{left:277px;top:31px;width:9px;height:9px;border-radius:50%;background:var(--white)}
.phone{left:402px;top:33px;font-size:18px;font-weight:300;color:var(--white);display:flex;align-items:center;gap:6px}
.quote-top{left:554px;top:35px;width:54px;height:19px;background:var(--white);color:var(--green-text);font-size:8px;text-align:center;line-height:19px}
.social{top:36px;width:18px;height:18px;border-radius:50%;background:var(--white);opacity:.9}
.nav{left:0;top:71px;width:866px;height:38px;background:linear-gradient(#fafafa,#e4e4e4);border-top:1px solid #fff;border-bottom:1px solid #d0d0d0}
.nav ul{list-style:none;position:absolute;left:180px;top:0;display:flex;height:37px}
.nav li{font-size:8.5px;color:#666;text-align:center;line-height:37px;border-right:1px solid #d4d4d4}
.nav li.active{background:#3b3b3b;color:#fff}
.nav li.green{background:var(--green);color:#fff;border-right-color:#6da300}
.nav li.hover{background:#dcdcdc;color:var(--green-text)}
.band{left:0;top:109px;width:866px;height:171px;background:var(--green)}
.column{left:180px;top:109px;width:506px;height:879px;background:#f4f4f4}
.slide{left:180px;top:110px;width:506px;height:200px;background:linear-gradient(100deg,#2d2d2d 0,#d9d9d9 18%,#efefef 45%,#cfcfcf 70%,#b5b5b5 100%)}
.arrow{top:195px;width:29px;height:29px;background:var(--green-dark);display:flex;align-items:center;justify-content:center}
.dots{left:411px;top:295px;display:flex;gap:5px;align-items:center}
.dots i{width:5px;height:5px;border-radius:50%;background:#555}
.dots i.on{width:9px;height:9px;background:var(--green)}
.tagline{left:310px;top:331px;font-size:11px;font-weight:300;color:var(--green-text)}
.quote-mid{left:502px;top:328px;width:53px;height:20px;background:var(--green);color:#fff;font-size:8px;text-align:center;line-height:20px}
.rule{left:180px;width:506px;height:2px;background:var(--green)}
.label{height:18px;background:var(--green);color:#fff;font-size:9.5px;font-weight:500;text-align:center;line-height:18px}
.services{left:180px;top:376px;width:506px;height:166px;display:flex}
.service{flex:1;text-align:center;padding-top:22px}
.service:nth-child(odd){background:#e3e3e3}
.service:nth-child(even){background:#ececec}
.service h3{font-size:10px;font-weight:400;color:var(--green-text);margin-top:8px}
.service p{font-size:6.5px;line-height:8px;color:var(--muted);padding:0 12px;margin-top:2px}
.why{top:571px;width:168px;height:175px;background:#ececec}
.why .pic{height:87px}
.why h3{height:20px;background:#e0e0e0;font-size:10px;font-weight:300;color:var(--green-text);padding:4px 6px;position:relative}
.why h3:after{content:"";position:absolute;left:0;bottom:-1px;width:90px;height:2px;background:var(--green)}
.why p{font-size:6.8px;line-height:8.6px;color:var(--muted);padding:7px 6px 0}
.why .more{position:absolute;right:0;bottom:0;width:50px;height:13px;background:var(--green);color:#fff;font-size:7px;text-align:center;line-height:13px}
.clients{left:180px;top:810px;display:flex;gap:4px}
.client{width:98px;height:54px;background:#fff;border:1px solid #dcdcdc;display:flex;align-items:center;justify-content:center;font-size:8px;color:#999;gap:4px}
.tabs{left:186px;top:884px;display:flex;gap:4px}
.tab{height:18px;padding:0 7px;background:#e2e2e2;font-size:7.5px;color:#555;line-height:18px}
.tab.on{background:#e9e9e9;color:var(--green-text);box-shadow:inset 0 0 0 3px #f4f4f4}
.tab-panel{left:186px;top:920px;width:330px;font-size:6.8px;color:#555;line-height:8.5px;list-style:none}
.tab-panel li{padding-left:7px;position:relative;margin-bottom:9px}
.tab-panel li:before{content:"";position:absolute;left:0;top:3px;width:2.5px;height:2.5px;border-radius:50%;background:#555}
.tab-panel a{color:#2233cc}
.footer{left:0;top:1002px;width:866px;height:198px;background:var(--footer)}
.cta{left:182px;top:988px;width:503px;height:30px;background:#fff;font-size:9.5px;font-weight:300;color:#333;text-align:center;line-height:30px}
.news{left:186px;top:1034px;width:174px;height:108px;background:var(--footer-box);padding:6px}
.news h4{font-size:9.5px;font-weight:300;color:#ddd}
.field{width:161px;height:17px;background:#fff;font-size:6.5px;color:#555;padding:5px;margin-top:6px}
.news p{font-size:6.5px;color:#bbb;line-height:8px;margin-top:4px}
.send{position:absolute;right:0;bottom:0;width:52px;height:17px;background:var(--green);color:#fff;font-size:9px;text-align:center;line-height:17px}
.fcol h4{font-size:9.5px;font-weight:300;color:#ddd;margin-bottom:7px}
.fcol li{list-style:none;font-size:6.5px;color:#bbb;margin-bottom:8px}
.fline{left:180px;top:1162px;width:506px;height:1px;background:#666}
.copy{left:186px;top:1173px;font-size:6.5px;color:#ccc}
</style>
</head>
<body>
<div class="abs topbar"></div>
<div class="abs account">KovaridexOnline™ <u>Login</u> ▾</div>
<div class="abs search">Search
  <svg width="10" height="10" viewBox="0 0 10 10"><circle cx="4" cy="4" r="3" fill="none" stroke="#6aa700" stroke-width="1.3"/><path d="M6.2 6.2 9 9" stroke="#6aa700" stroke-width="1.3"/></svg>
</div>
<div class="abs header"></div>
<div class="abs logo">Kovaridex</div>
<div class="abs logo-dot"></div>
<div class="abs phone">
  <svg width="12" height="12" viewBox="0 0 12 12"><path d="M2.5 1 4.5 1 5.3 3.6 4 4.6C4.7 6.2 5.8 7.3 7.4 8L8.4 6.7 11 7.5 11 9.5C11 10.3 10.3 11 9.5 11 5 11 1 7 1 2.5 1 1.7 1.7 1 2.5 1Z" fill="#fff"/></svg>
  1-800-000-0000
</div>
<div class="abs quote-top">Get a Quote</div>
<div class="abs social" style="left:614px" role="img" aria-label="Social link"></div>
<div class="abs social" style="left:639px" role="img" aria-label="Social link"></div>
<div class="abs social" style="left:663px" role="img" aria-label="Social link"></div>

<nav class="abs nav"><ul>
  <li class="active" style="width:60px">Services</li>
  <li class="green" style="width:70px">Solutions</li>
  <li class="green" style="width:85px">Why us</li>
  <li class="hover" style="width:58px">About</li>
  <li style="width:60px">Partner</li>
  <li style="width:59px">Events</li>
  <li style="width:64px">Contact</li>
  <li style="width:50px">Blog</li>
</ul></nav>

<div class="abs band"></div>
<div class="abs column"></div>
<div class="abs slide" role="img" aria-label="Photo of a spiral notebook with the cloud phone system promo, a pen and a laptop keyboard"></div>
<div class="abs arrow" style="left:165px"><svg width="10" height="16" viewBox="0 0 10 16"><path d="M8 1 2 8 8 15" fill="none" stroke="#fff" stroke-width="2"/></svg></div>
<div class="abs arrow" style="left:671px"><svg width="10" height="16" viewBox="0 0 10 16"><path d="M2 1 8 8 2 15" fill="none" stroke="#fff" stroke-width="2"/></svg></div>
<div class="abs dots"><i></i><i class="on"></i><i></i><i></i></div>

<div class="abs tagline">The only technology partner you need.</div>
<div class="abs quote-mid">Get a Quote</div>

<div class="abs rule" style="top:372px"></div>
<div class="abs label" style="left:375px;top:364px;width:116px">OUR SERVICES</div>
<section class="abs services">
  <div class="service">
    <svg width="46" height="42" viewBox="0 0 46 42"><circle cx="20" cy="23" r="19" fill="#80bd01"/><circle cx="36" cy="6" r="4" fill="#80bd01"/><circle cx="30" cy="2.5" r="2.3" fill="#80bd01"/><path d="M12 29h15a5 5 0 0 0 0-10 7 7 0 0 0-13 1 4.5 4.5 0 0 0-2 9Z" fill="#fff"/></svg>
    <h3>CLOUD</h3><p>Lorem Ipsum is simply dummy text of the printing and typesetting industry.</p>
  </div>
  <div class="service">
    <svg width="46" height="42" viewBox="0 0 46 42"><circle cx="20" cy="23" r="19" fill="#80bd01"/><circle cx="36" cy="6" r="4" fill="#80bd01"/><circle cx="30" cy="2.5" r="2.3" fill="#80bd01"/><path d="M11 26v-4a9 9 0 0 1 18 0v4" fill="none" stroke="#fff" stroke-width="2.5"/><rect x="9" y="23" width="5" height="8" rx="1.5" fill="#fff"/><rect x="26" y="23" width="5" height="8" rx="1.5" fill="#fff"/></svg>
    <h3>VOICE</h3><p>Lorem Ipsum is simply dummy text of the printing and typesetting industry.</p>
  </div>
  <div class="service">
    <svg width="46" height="42" viewBox="0 0 46 42"><circle cx="20" cy="23" r="19" fill="#80bd01"/><circle cx="36" cy="6" r="4" fill="#80bd01"/><circle cx="30" cy="2.5" r="2.3" fill="#80bd01"/><rect x="15" y="13" width="10" height="19" rx="2" fill="#fff"/><rect x="17" y="16" width="6" height="5" fill="#80bd01"/><path d="M17 24h6M17 27h6M17 30h6" stroke="#80bd01" stroke-width="1"/></svg>
    <h3>MOBILE</h3><p>Lorem Ipsum is simply dummy text of the printing and typesetting industry.</p>
  </div>
  <div class="service">
    <svg width="46" height="42" viewBox="0 0 46 42"><circle cx="20" cy="23" r="19" fill="#80bd01"/><circle cx="36" cy="6" r="4" fill="#80bd01"/><circle cx="30" cy="2.5" r="2.3" fill="#80bd01"/><circle cx="20" cy="21" r="2.5" fill="#fff"/><path d="M20 23v10M15 17a7 7 0 0 0 0 8M25 17a7 7 0 0 1 0 8M12 14a11 11 0 0 0 0 14M28 14a11 11 0 0 1 0 14" fill="none" stroke="#fff" stroke-width="2"/></svg>
    <h3>NETWORK</h3><p>Lorem Ipsum is simply dummy text of the printing and typesetting industry.</p>
  </div>
  <div class="service">
    <svg width="46" height="42" viewBox="0 0 46 42"><circle cx="20" cy="23" r="19" fill="#80bd01"/><circle cx="36" cy="6" r="4" fill="#80bd01"/><circle cx="30" cy="2.5" r="2.3" fill="#80bd01"/><path d="M10 18h20v4H10Z M12 23h16v9H12Z M10 18l5-5h10l5 5" fill="#fff"/><path d="M20 18v14" stroke="#80bd01" stroke-width="1.5"/></svg>
    <h3>APPLCATIONS</h3><p>Lorem Ipsum is simply dummy text of the printing and typesetting industry.</p>
  </div>
</section>

<div class="abs rule" style="top:542px"></div>
<div class="abs label" style="left:375px;top:533px;width:116px">WHY KOVARIDEX</div>

<article class="abs why" style="left:180px">
  <div class="pic" role="img" aria-label="Illustration of a hand touching a cloud computing network of devices" style="background:radial-gradient(circle at 50% 45%,#7fd0f5,#1c8fd6 75%)"></div>
  <h3>About Kovaridex</h3>
  <p>Lorem Ipsum is simply dummy text of the printing and typesetting industry. Lorem Ipsum is simply dummy text of the printing and typesetting industry.</p>
  <span class="more">Learn more</span>
</article>
<article class="abs why" style="left:349px">
  <div class="pic" role="img" aria-label="Photo of a businesswoman beside a sketched cloud computing diagram" style="background:linear-gradient(90deg,#f6f6f6,#ece6dc 70%,#e2d6c4)"></div>
  <h3>What we offer</h3>
  <p>Lorem Ipsum is simply dummy text of the printing and typesetting industry. Lorem Ipsum is simply dummy text of the printing and typesetting industry.</p>
  <span class="more">Learn more</span>
</article>
<article class="abs why" style="left:518px">
  <div class="pic" role="img" aria-label="Photo of a hand ticking a feedback rating checklist" style="background:linear-gradient(90deg,#f4f4f4 55%,#c9c9c9 80%,#4a4a4a)"></div>
  <h3>Client Testimonials</h3>
  <p>Lorem Ipsum is simply dummy text of the printing and typesetting industry. Lorem Ipsum is simply dummy text of the printing and typesetting industry.</p>
  <span class="more">Learn more</span>
</article>

<div class="abs rule" style="top:776px"></div>
<div class="abs label" style="left:388px;top:768px;width:90px">OUR CLIENTS</div>
<div class="abs clients">
  <div class="client">Frostvale</div>
  <div class="client">Strivo</div>
  <div class="client">Talvern Mobile</div>
  <div class="client">Eastmark Pay</div>
  <div class="client">Fizzbrook</div>
</div>

<div class="abs tabs">
  <div class="tab on">Our Service</div>
  <div class="tab">Our Suport</div>
  <div class="tab">Our People</div>
</div>
<ul class="abs tab-panel">
  <li>Lorem Ipsum is simply dummy text of the printing and typesetting<br>industry.</li>
  <li>Lorem Ipsum is simply dummy text of the printing and <a href="#"><u>typesetting industry.</u></a></li>
  <li>Lorem Ipsum is simply dummy text of the printing and typesetting industry.</li>
</ul>

<footer class="abs footer"></footer>
<div class="abs cta">Ready to take your business to the next level? Contact us today.</div>
<form class="abs news">
  <h4>Subscribe to our Newsletter</h4>
  <div class="field" style="margin-top:4px">Full Name</div>
  <div class="field">Email</div>
  <p>Lorem Ipsum is simply dummy text of the printing and typesetting industry.</p>
  <span class="send">SEND</span>
</form>
<div class="abs fcol" style="left:437px;top:1040px"><h4>Solutions</h4><ul><li>Industry Solutions</li><li style="margin-top:10px">Managed Solutions</li><li style="margin-top:10px">Security Solutions</li></ul></div>
<div class="abs fcol" style="left:524px;top:1040px"><h4>Services</h4><ul><li>Cloud</li><li>Voice</li><li>Mobile</li><li>Network</li><li>Applications</li></ul></div>
<div class="abs fcol" style="left:587px;top:1040px"><h4>Why Kovaridex</h4><ul><li>About</li><li>Careers</li><li>Events</li><li>Blog</li><li>Product Tours</li></ul></div>
<div class="abs fline"></div>
<div class="abs copy">© 2012-2013 Kovaridex.&nbsp;&nbsp; Privacy &nbsp;|&nbsp; Legal</div>
</body>
</html>
```